Coral Sleep Depot Website

Need a design for a local Coral Sleep Depot store.
The store is called Coral Sleep Depot.
need it to be something that customers can find on the internet and will
give them my location, they need to know i have the same brand mattress as the other store except i have them at almost half the price.

the office phone number is (786)555-0143
the office address is: 4127 sw Heron Bend Ave, Miami FL 33190

included is the logo, id like to stick the with white and teal design

here are is an excerpt that can or cannot be included

"We are a premium mattress discount outlet store located in South Florida; offering Free Delivery to Broward Miami-Dade, the Keys, and Palm Beach.

We carry the best brands in the market: Varnell CloudHaven; Dorvik SpineAlign, Brackett & Lowe, Pendry, among others.

We are open 7 days a week, and we are accessible from all major highways. We are a family business and our goal is to provide you with the most comfortable and best quality mattress at a price that has no competition. Come visit us and take a look at our large inventory selection."

```html
<!DOCTYPE html>
<html lang="en">
<head>
<meta charset="utf-8">
<title>Coral Sleep Depot</title>
<link href="https://fonts.googleapis.com/css2?family=Montserrat:wght@400;500;700&family=Roboto:wght@400;700&display=swap" rel="stylesheet">
<style>
:root{
  --teal:#00b3cc;
  --teal-light:#1fd0ea;
  --dark:#262626;
  --cream:#f4f2e8;
  --cream-border:#c9c7bd;
  --text:#333333;
  --white:#ffffff;
  --gold:#f5a623;
  --green:#1d7a52;
}
*{box-sizing:border-box;margin:0;padding:0}
html,body{width:1200px;height:2168px;overflow:hidden}
body{position:relative;background:var(--white);font-family:"Montserrat",sans-serif;color:var(--text)}
.abs{position:absolute}

/* top bar */
.topbar{left:0;top:0;width:1200px;height:48px;background:var(--dark)}
.topbar-accent{left:0;top:48px;width:1200px;height:8px;background:var(--teal)}
.social{left:128px;top:10px;display:flex;gap:6px}
.social span{width:26px;height:26px;border-radius:3px;background:#4a4a4a;display:block}
.callus{right:128px;top:6px;display:flex;align-items:center;gap:10px;font-size:21px;font-weight:700;color:var(--white)}
.callus .number{color:var(--teal);margin-left:8px}

/* header */
.brand{left:128px;top:92px;display:flex;align-items:center;gap:12px;font-size:27px;font-weight:500;color:var(--dark)}
.brand .mark{width:22px;height:22px;background:var(--teal)}
.nav{left:440px;top:59px;display:flex;font-size:20px}
.nav a{display:block;padding:0 10px;height:69px;line-height:98px;color:var(--text);text-decoration:none}
.nav a.active{background:var(--cream);color:var(--teal);border-bottom:2px solid #d8d5c4;width:80px;text-align:center;padding:0}
.cart{left:1005px;top:93px;width:64px;height:38px;background:var(--cream);display:flex;align-items:center;justify-content:center;gap:6px;font-size:14px;color:#555}

/* hero */
.hero{left:128px;top:187px;width:941px;height:343px;border-radius:5px;overflow:hidden;background:var(--teal)}
.hero-photo{left:0;top:0;width:528px;height:343px;background:linear-gradient(135deg,#5b4a3a 0%,#8b7a66 40%,#d9d2c6 60%,#3a2c22 100%);clip-path:polygon(0 0,405px 0,528px 343px,0 343px)}
.hero-copy{left:540px;top:26px;width:322px;text-align:center;color:var(--white);font-size:19.5px;font-weight:500;line-height:35px}
.hero-btn{left:606px;top:232px;width:196px;height:56px;background:#f5f3ea;border-radius:5px;font-size:25px;color:var(--dark);display:flex;align-items:center;justify-content:center}

/* section headings */
.section-title{left:128px;width:944px;text-align:center;font-size:36px;font-variant:small-caps;letter-spacing:1px;color:var(--dark);font-weight:400}
.section-rule{left:128px;width:944px;height:6px;background:var(--teal)}

/* carousel */
.card{width:220px;height:288px;background:var(--cream);top:770px}
.card .thumb{position:absolute;left:8px;top:8px;width:204px;height:138px;border:1px solid #aaa;background:linear-gradient(180deg,#fafafa 0%,#e6e2d8 55%,#fafafa 100%)}
.card .name{position:absolute;top:163px;width:100%;text-align:center;font-size:21px}
.card .add{position:absolute;left:26px;top:220px;width:170px;height:53px;border-radius:4px;background:var(--teal);color:var(--white);font-size:21px;display:flex;align-items:center;justify-content:center}
.arrow-btn{top:890px;width:26px;height:37px;border:1px solid #bbb;background:var(--white)}

/* sidebar */
.filter{left:133px;width:200px;height:51px;background:var(--cream);border:1px solid var(--cream-border);font-size:21px;color:#555;text-align:center;line-height:56px}
.filter.active{background:var(--teal);color:var(--white);border-color:var(--teal);font-weight:500;padding-right:20px}
.filter.active svg{position:absolute;right:12px;top:16px}

/* product grid */
.product{width:171px;height:164px;border:1px solid #1a8fb0;background:linear-gradient(180deg,#fff 0%,#e9e7e2 60%,#fff 100%)}
.product .rating{position:absolute;left:0;bottom:0;width:100%;height:45px;background:var(--teal);display:flex;align-items:center;justify-content:center}
.product .tag{position:absolute;left:0;top:0;padding:3px 8px;background:var(--cream);font-size:14px}
.price{width:171px;text-align:center;font-size:14px;font-family:"Roboto",sans-serif;color:#111}
.next{left:936px;top:1800px;display:flex;align-items:center;gap:8px;color:var(--teal);font-size:18px}

/* footer */
.footer{left:0;top:1922px;width:1200px;height:246px;background:var(--dark);font-family:"Roboto",sans-serif}
.fhead{height:30px;background:linear-gradient(180deg,var(--teal-light),var(--teal));color:var(--white);font-size:11px;font-weight:700;line-height:30px;padding-left:10px;border-radius:2px}
.ftext{color:var(--white);font-size:11px;line-height:16px}
.show-me{width:84px;height:26px;background:var(--green);border-radius:2px;color:var(--white);font-size:10px;display:flex;align-items:center;justify-content:center;gap:8px}
.map{left:802px;top:24px;width:251px;height:137px;background:var(--white);padding:5px;border-radius:2px}
.map div{width:100%;height:100%;background:linear-gradient(135deg,#e8e4da,#d8e6cf 50%,#c9dbe8)}
.frule{left:128px;top:187px;width:922px;height:1px;background:#3d5a4a}
.copyright{left:132px;top:209px;color:var(--white);font-size:10px}
.flinks{left:632px;top:209px;color:var(--white);font-size:10px;word-spacing:4px}
</style>
</head>
<body>

<div class="abs topbar"></div>
<div class="abs topbar-accent"></div>
<div class="abs social" aria-label="Social links"><span></span><span></span><span></span><span></span></div>
<div class="abs callus">
  <svg width="28" height="28" viewBox="0 0 28 28"><rect width="28" height="28" rx="4" fill="#fff"/><path d="M9 6c1 0 2 3 2 4s-2 1-2 2 3 5 5 5 1-2 2-2 4 1 4 2-1 4-3 4C11 21 7 14 7 9c0-2 1-3 2-3z" fill="#262626"/></svg>
  <span>Call Us</span><span class="number">(786)555-0143</span>
</div>

<div class="abs brand"><span class="mark"></span>Coral Sleep Depot</div>

<nav class="abs nav">
  <a class="active" href="#">Home</a>
  <a href="#">Products</a>
  <a href="#">About Us</a>
  <a href="#">Contct Us</a>
</nav>
<div class="abs cart">(0)
  <svg width="22" height="18" viewBox="0 0 22 18"><path d="M1 2h4l3 10h10l3-8H7" fill="none" stroke="#222" stroke-width="2"/><circle cx="9" cy="15.5" r="1.8" fill="#222"/><circle cx="17" cy="15.5" r="1.8" fill="#222"/></svg>
</div>

<section class="abs hero">
  <div class="abs hero-photo" role="img" aria-label="Photo of a hotel-style bedroom with a made bed"></div>
  <p class="abs hero-copy">We carry the best brands in the market: Varnell CloudHaven; Dorvik SpineAlign, Brackett &amp; Lowe, Pendry, among others</p>
  <div class="abs hero-btn">Shop now</div>
</section>

<h2 class="abs section-title" style="top:640px">Some of our mattresses</h2>
<div class="abs section-rule" style="top:710px"></div>

<div class="abs arrow-btn" style="left:158px"><svg width="24" height="35" viewBox="0 0 24 35"><path d="M15 10l-7 7.5 7 7.5" fill="none" stroke="#999" stroke-width="2"/></svg></div>
<div class="abs card" style="left:238px"><div class="thumb" role="img" aria-label="Mattress photo"></div><div class="name">Lorem Lipsum</div><div class="add">Add to cart</div></div>
<div class="abs card" style="left:491px"><div class="thumb" role="img" aria-label="Mattress photo"></div><div class="name">Vestibulum</div><div class="add">Add to cart</div></div>
<div class="abs card" style="left:742px"><div class="thumb" role="img" aria-label="Mattress photo"></div><div class="name">Ropsum</div><div class="add">Add to cart</div></div>
<div class="abs arrow-btn" style="left:1010px"><svg width="24" height="35" viewBox="0 0 24 35"><path d="M9 10l7 7.5-7 7.5" fill="none" stroke="#999" stroke-width="2"/></svg></div>

<h2 class="abs section-title" style="top:1183px">Our products</h2>
<div class="abs section-rule" style="top:1242px"></div>

<div class="abs filter active" style="top:1307px">Best Seller<svg width="12" height="20" viewBox="0 0 12 20"><path d="M2 2l7 8-7 8" fill="none" stroke="#fff" stroke-width="2.5"/></svg></div>
<div class="abs filter" style="top:1365px">King</div>
<div class="abs filter" style="top:1422px">Queen</div>
<div class="abs filter" style="top:1480px">Twin</div>
<div class="abs filter" style="top:1538px">Single</div>

<svg width="0" height="0" style="position:absolute">
  <defs>
    <path id="star" d="M10 1l2.7 5.6 6.1.9-4.4 4.3 1 6.1L10 15l-5.4 2.9 1-6.1L1.2 7.5l6.1-.9z"/>
    <g id="stars">
      <use href="#star" x="0" fill="#f5a623" stroke="#c77d00"/>
      <use href="#star" x="21" fill="#f5a623" stroke="#c77d00"/>
      <use href="#star" x="42" fill="#f5a623" stroke="#c77d00"/>
      <use href="#star" x="63" fill="#f5a623" stroke="#c77d00"/>
      <use href="#star" x="84" fill="#ffffff" stroke="#aaa"/>
    </g>
  </defs>
</svg>

<div class="abs product" style="left:437px;top:1342px" role="img" aria-label="Mattress photo"><span class="tag">Add to cart</span><div class="rating"><svg width="106" height="20" viewBox="0 0 106 20"><use href="#stars"/></svg></div></div>
<div class="abs product" style="left:645px;top:1342px" role="img" aria-label="Mattress photo"><div class="rating"><svg width="106" height="20" viewBox="0 0 106 20"><use href="#stars"/></svg></div></div>
<div class="abs product" style="left:851px;top:1342px" role="img" aria-label="Mattress photo"><div class="rating"><svg width="106" height="20" viewBox="0 0 106 20"><use href="#stars"/></svg></div></div>
<div class="abs price" style="left:437px;top:1528px">$220.00</div>
<div class="abs price" style="left:645px;top:1528px">$220.00</div>
<div class="abs price" style="left:851px;top:1528px">$220.00</div>

<div class="abs product" style="left:437px;top:1570px" role="img" aria-label="Mattress photo"><div class="rating"><svg width="106" height="20" viewBox="0 0 106 20"><use href="#stars"/></svg></div></div>
<div class="abs product" style="left:645px;top:1570px" role="img" aria-label="Mattress photo"><div class="rating"><svg width="106" height="20" viewBox="0 0 106 20"><use href="#stars"/></svg></div></div>
<div class="abs product" style="left:851px;top:1570px" role="img" aria-label="Mattress photo"><div class="rating"><svg width="106" height="20" viewBox="0 0 106 20"><use href="#stars"/></svg></div></div>
<div class="abs price" style="left:437px;top:1755px">$220.00</div>
<div class="abs price" style="left:645px;top:1755px">$220.00</div>
<div class="abs price" style="left:851px;top:1755px">$220.00</div>

<div class="abs next">Next Page<svg width="28" height="24" viewBox="0 0 28 24"><path d="M3 3l9 9-9 9M14 3l9 9-9 9" fill="none" stroke="#555" stroke-width="3"/></svg></div>

<footer class="abs footer">
  <div class="abs" style="left:146px;top:24px;width:232px">
    <div class="fhead">About Us</div>
    <p class="ftext" style="margin-top:14px;font-weight:700">Pellentesque accumsan dignissim libero eu dignissim. Aliquam sed accumsan tortor. Aenean ultrices lectus a malesuada consequat.</p>
    <div class="show-me" style="margin:14px 0 0 10px">show me<svg width="7" height="10" viewBox="0 0 7 10"><path d="M1 1l4 4-4 4" fill="none" stroke="#fff" stroke-width="2"/></svg></div>
  </div>
  <div class="abs" style="left:414px;top:24px;width:157px">
    <div class="fhead" style="color:#111">MENU</div>
    <p class="ftext" style="margin:10px 0 0 12px;line-height:21px">About us<br>Services<br>Solutions<br>Prices<br>Contact</p>
  </div>
  <div class="abs" style="left:608px;top:24px;width:190px">
    <div class="fhead" style="width:157px;color:#111">CONTACT</div>
    <p class="ftext" style="margin:10px 0 0 14px;line-height:21px">4127 sw Heron Bend Ave,<br>Miami FL 33190<br>United States<br>e-mail: info@coralsleepdepot.com</p>
  </div>
  <div class="abs map"><div role="img" aria-label="Street map showing the store location"></div></div>
  <div class="abs frule"></div>
  <p class="abs copyright">Copyright 2014 | Coral Sleep Depot | All rights reserved</p>
  <p class="abs flinks">About / News / Privacy / Security / Terms</p>
</footer>

</body>
</html>
```